Real Estate Development Company Stationary

We need our company, business card, letterhead, pocket folder and envelope designed.

We are a new real estate development company. We focus on data centre, commercial and real estate development.

Please see attached for our logo. Since it's a new logo, you still can make minor adjust if you like it makes senses

The client has sent me a business card he really likes. Please see file 3.

Target Market(s)

Real Estate Investors
Large corporations
Home buyers

Industry/Entity Type

Real Estate

```html
<!DOCTYPE html>
<html lang="en">
<head>
<meta charset="utf-8">
<title>Norvale Development Inc. — Stationery</title>
<link rel="stylesheet" href="https://fonts.googleapis.com/css2?family=Lato:wght@400;700&display=swap">
<style>
  :root {
    --stage: #000000;
    --paper: #ffffff;
    --brand-green: #71bf44;
    --brand-navy: #1f4e8c;
    --tint-lavender: #cfd3ea;
    --tint-green: #e5f0da;
    --ink: #555555;
    --edge: #b5b5b5;
    --label: #ffffff;
  }
  * { box-sizing: border-box; margin: 0; padding: 0; }
  html, body {
    width: 1200px;
    height: 986px;
    overflow: hidden;
    background: var(--stage);
    font-family: "Lato", Arial, sans-serif;
  }
  .canvas { position: relative; width: 1200px; height: 986px; }

  .sheet { position: absolute; background: var(--paper); overflow: hidden; }
  .sheet__band { position: absolute; left: 0; right: 0; bottom: 0; background: var(--brand-green); z-index: 1; }

  .sheet__tint {
    position: absolute;
    border-radius: 50%;
    background: linear-gradient(135deg, var(--tint-lavender) 0%, var(--tint-lavender) 45%, var(--tint-green) 55%, var(--tint-green) 100%);
    opacity: 0.85;
  }

  .brand { position: absolute; display: flex; align-items: center; z-index: 2; }
  .brand__dot { border-radius: 50%; background: var(--brand-navy); flex: none; }
  .brand__name { color: var(--brand-green); font-weight: 700; white-space: nowrap; line-height: 1.05; }

  .address { position: absolute; color: var(--ink); line-height: 1.4; font-style: normal; z-index: 2; }

  .letterhead { left: 63px; top: 45px; width: 674px; height: 872px; z-index: 1; }
  .letterhead .sheet__band { height: 44px; }
  .letterhead .sheet__tint { left: 283px; top: 345px; width: 470px; height: 470px; }
  .letterhead .brand { left: 24px; top: 28px; gap: 10px; }
  .letterhead .brand__dot { width: 30px; height: 30px; }
  .letterhead .brand__name { font-size: 18px; }
  .letterhead .address { left: 23px; top: 746px; font-size: 11px; line-height: 1.38; }

  .envelope { left: 465px; top: 83px; width: 663px; height: 332px; border: 1px solid var(--edge); z-index: 2; }
  .envelope .sheet__band { height: 33px; }
  .envelope .sheet__tint { left: 475px; top: 60px; width: 220px; height: 220px; }
  .envelope .brand { left: 18px; top: 18px; gap: 8px; }
  .envelope .brand__dot { width: 24px; height: 24px; }
  .envelope .brand__name { font-size: 13px; }
  .envelope .address { left: 19px; top: 58px; font-size: 8.5px; line-height: 1.36; }

  .business-card { left: 809px; top: 493px; width: 319px; height: 182px; border: 1px solid var(--edge); }
  .business-card .sheet__band { height: 19px; }
  .business-card .sheet__tint { left: 218px; top: 30px; width: 120px; height: 120px; }
  .business-card .brand { left: 13px; top: 18px; gap: 8px; }
  .business-card .brand__dot { width: 24px; height: 24px; }
  .business-card .brand__name { font-size: 12px; }
  .business-card .holder { position: absolute; left: 143px; top: 82px; font-size: 13px; color: var(--ink); letter-spacing: 0.2px; z-index: 2; }
  .business-card .address { left: 14px; top: 111px; font-size: 7.5px; line-height: 1.5; }

  .label { position: absolute; color: var(--label); font-weight: 700; font-size: 16px; letter-spacing: 0.5px; }
  .label--letterhead { left: 62px; top: 930px; }
  .label--envelope { right: 72px; top: 426px; }
  .label--card { left: 899px; top: 693px; }
</style>
</head>
<body>
<main class="canvas">

  <section class="sheet letterhead" aria-label="Letterhead">
    <div class="sheet__tint" role="img" aria-label="Large faint brand decoration"></div>
    <div class="brand">
      <span class="brand__dot"></span>
      <span class="brand__name">Norvale Development Inc.</span>
    </div>
    <address class="address">
      0000 Maple Crest Way<br>
      Brookfield Ontario<br>
      P.O Box 0000, CA<br>
      Tel: (555) 0000-0000
    </address>
    <div class="sheet__band"></div>
  </section>

  <section class="sheet envelope" aria-label="Envelope">
    <div class="sheet__tint" role="img" aria-label="Faint brand decoration"></div>
    <div class="brand">
      <span class="brand__dot"></span>
      <span class="brand__name">Norvale Development Inc.</span>
    </div>
    <address class="address">
      0000 Maple Crest Way<br>
      Brookfield Ontario<br>
      P.O Box 0000, CA
    </address>
    <div class="sheet__band"></div>
  </section>

  <section class="sheet business-card" aria-label="Business card">
    <div class="sheet__tint" role="img" aria-label="Faint brand decoration"></div>
    <div class="brand">
      <span class="brand__dot"></span>
      <span class="brand__name">Norvale Development Inc.</span>
    </div>
    <p class="holder">MIRA OLSEN</p>
    <address class="address">
      0000 Maple Crest Way<br>
      Brookfield Ontario<br>
      P.O Box 0000, CA<br>
      Tel: (555) 0000-0000
    </address>
    <div class="sheet__band"></div>
  </section>

  <p class="label label--envelope">ENVELOPE</p>
  <p class="label label--card">BUSINESS CARD</p>
  <p class="label label--letterhead">LETTERHEAD</p>

</main>
</body>
</html>
```